School and office cleaning at its best

We need a flyer for our mailing purposes to obtain new customers. Our name of the company is The Brightwells We have been in business since 2008 and are servicing multiple locations in san Jose CA our primary colors are black and white and red
We are servicing schools, offices, office buildings, gyms, dance studios,
We provide janitorial services weekly,biweekly and daily.
We have uniformed custodians.
We also provide carpet cleaning
Floors strip and wax
Floor steaming
Personal supervision
Quality control

Target Market(s)

Offices, schools, gyms, office buildings

Industry/Entity Type

Janitorial Service

Font styles to use
Serif

Colors

Designer to choose colors to be used in the design.

Requirements
Must have
• services provided
• Cleaning
• Carpet cleaning
• Floor strip and wax
• Floor steaming
• Janitorial services
• \Uniformed custodians
Nice to have
• surprise me
• Colors of black
• red
• white
• among others
Should not have
• Prices
• discounts

```html
<!DOCTYPE html>
<html lang="en">
<head>
<meta charset="utf-8">
<title>The Brightwells – Cleaning Services Flyer</title>
<link href="https://fonts.googleapis.com/css2?family=Oswald:wght@400;500;600&family=Roboto:ital,wght@0,400;0,500;1,400&display=swap" rel="stylesheet">
<style>
  :root{
    --red:#c8202a;
    --black:#0b0b0b;
    --white:#ffffff;
    --ink:#1c1c1c;
    --silver-1:#f4f4f4;
    --silver-2:#bdbdbd;
    --photo-blue:#5f9fd6;
    --photo-grey:#d9dde2;
    --photo-navy:#3b4456;
  }
  *{margin:0;padding:0;box-sizing:border-box}
  html,body{width:1200px;height:902px;overflow:hidden;background:var(--white)}
  .flyer{position:relative;width:1200px;height:902px;overflow:hidden;background:var(--white);font-family:"Roboto",Arial,sans-serif}
  .backdrop{position:absolute;inset:0}
  .brand{position:absolute;left:48px;top:82px;width:327px;height:283px;background:#111;display:flex;flex-direction:column;align-items:center;justify-content:center;gap:8px}
  .brand__name{font-family:"Oswald",Arial,sans-serif;font-weight:600;color:var(--white);font-size:46px;line-height:1;text-align:center}
  .brand__mark{width:22px;height:22px;border-radius:50%;background:var(--red)}
  .headline{position:absolute;left:500px;top:46px;width:700px;display:flex;justify-content:center;white-space:nowrap;font-family:"Oswald",Arial,sans-serif;font-weight:500;font-size:82px;line-height:1;color:var(--white);letter-spacing:1px}
  .sectors{position:absolute;left:400px;top:160px;width:790px;height:52px;display:flex;align-items:center;justify-content:center;white-space:nowrap;color:var(--white);font-size:22px;letter-spacing:.5px}
  .photo{position:absolute;border-radius:4px}
  .photo--team{left:452px;top:232px;width:436px;height:325px;background:linear-gradient(180deg,var(--photo-grey) 0%,var(--photo-blue) 45%,#3c4a63 100%)}
  .photo--custodian{left:940px;top:460px;width:226px;height:390px;background:linear-gradient(180deg,#eef0f2 0%,var(--photo-navy) 40%,#e3823a 80%,#f0c53a 100%)}
  .frequency{position:absolute;left:905px;top:288px;width:215px;text-align:center;font-size:26px;line-height:1.3;color:var(--ink)}
  .frequency__lead{color:var(--red)}
  .badge{position:absolute;left:83px;top:428px;width:270px;height:270px;border-radius:50%;background:var(--red);display:flex;align-items:center;justify-content:center}
  .badge__inner{width:244px;height:244px;border-radius:50%;background:radial-gradient(circle at 50% 30%,var(--silver-1) 0%,#e4e4e4 60%,var(--silver-2) 100%);display:flex;flex-direction:column;align-items:center;justify-content:center;text-align:center;font-family:"Oswald",Arial,sans-serif;color:var(--ink)}
  .badge__small{font-size:24px;line-height:1.2;font-weight:500}
  .badge__city{font-size:38px;line-height:1.15;font-weight:500}
  .badge__since{font-size:30px;color:var(--red);font-weight:500;margin-top:8px}
  .call{position:absolute;left:0;width:440px;top:728px;text-align:center;color:var(--white);font-size:28px}
  .phone{position:absolute;left:40px;top:782px;display:flex;align-items:center;gap:16px;color:var(--white);font-family:"Oswald",Arial,sans-serif;font-weight:600;font-size:50px;line-height:1}
  .phone svg{width:44px;height:44px}
  .custodians{position:absolute;z-index:2;left:732px;top:567px;width:320px;height:58px;padding-left:18px;display:flex;align-items:center;justify-content:center;white-space:nowrap;background:var(--red);clip-path:polygon(23px 0,100% 0,100% 100%,0 100%);color:var(--white);font-family:"Oswald",Arial,sans-serif;font-weight:500;font-size:24px}
  .services__title{position:absolute;left:375px;top:636px;font-size:33px;font-weight:400;color:var(--ink);letter-spacing:.5px;white-space:nowrap}
  .services__title span{color:var(--red)}
  .services__list{position:absolute;list-style:none;font-style:italic;font-size:21px;color:var(--ink);white-space:nowrap}
  .services__list li{display:flex;align-items:center;gap:12px;height:41px}
  .services__list svg{width:22px;height:22px;flex:none}
  .services__list--a{left:432px;top:694px}
  .services__list--b{left:682px;top:694px}
</style>
</head>
<body>
<div class="flyer">
  <svg class="backdrop" width="1200" height="902" viewBox="0 0 1200 902" aria-hidden="true">
    <polygon points="0,0 505,0 337,563 0,563" fill="var(--black)"/>
    <polygon points="505,0 545,0 375,563 337,563" fill="var(--red)"/>
    <polygon points="0,563 340,563 407,902 0,902" fill="var(--red)"/>
    <polygon points="505,0 1200,0 1200,150 460,150" fill="var(--red)"/>
    <polygon points="410,156 1196,156 1196,214 392,214" fill="var(--black)" stroke="var(--white)" stroke-width="3"/>
    <polygon points="345,583 740,583 722,609 345,609" fill="var(--black)"/>
  </svg>

  <div class="brand">
    <div class="brand__mark"></div>
    <div class="brand__name">The Brightwells</div>
  </div>

  <h1 class="headline">CLEANING SERVICES</h1>
  <div class="sectors">SCHOOLS, OFFICES, OFFICE BUILDINGS, GYMS, DANCE STUDIOS</div>

  <div class="photo photo--team" role="img" aria-label="Photo of a smiling cleaning team in blue aprons with vacuum, mop and cleaning cart"></div>

  <p class="frequency"><span class="frequency__lead">We provide<br>janitorial services</span><br>weekly, biweekly<br>and daily</p>

  <div class="badge">
    <div class="badge__inner">
      <div class="badge__small">SERVICING</div>
      <div class="badge__small">MULTIPLE LOCATIONS IN</div>
      <div class="badge__city">SAN JOSE CA</div>
      <div class="badge__since">SINCE 2008</div>
    </div>
  </div>

  <p class="call">Call us today!</p>
  <div class="phone">
    <svg viewBox="0 0 44 44" aria-hidden="true">
      <circle cx="22" cy="22" r="19" fill="none" stroke="var(--black)" stroke-width="3"/>
      <path d="M15 12c1-1 3-1 4 0l2 4c.5 1 0 2-1 3l-1 1c1 3 3 5 6 6l1-1c1-1 2-1.5 3-1l4 2c1 1 1 3 0 4l-2 2c-8 0-16-8-16-16z" fill="var(--black)"/>
    </svg>
    <span>408 555 0142</span>
  </div>

  <div class="photo photo--custodian" role="img" aria-label="Photo of a uniformed custodian operating an orange floor buffer beside a yellow wet floor sign"></div>
  <div class="custodians">UNIFORMED CUSTODIANS</div>

  <h2 class="services__title"><span>SERVICES</span> PROVIDED</h2>
  <ul class="services__list services__list--a">
    <li><svg viewBox="0 0 24 24" aria-hidden="true"><rect x="2" y="4" width="17" height="17" fill="none" stroke="var(--ink)" stroke-width="2"/><path d="M6 12l4 4 11-12" fill="none" stroke="var(--red)" stroke-width="3.5"/></svg>Cleaning</li>
    <li><svg viewBox="0 0 24 24" aria-hidden="true"><rect x="2" y="4" width="17" height="17" fill="none" stroke="var(--ink)" stroke-width="2"/><path d="M6 12l4 4 11-12" fill="none" stroke="var(--red)" stroke-width="3.5"/></svg>Carpet cleaning</li>
    <li><svg viewBox="0 0 24 24" aria-hidden="true"><rect x="2" y="4" width="17" height="17" fill="none" stroke="var(--ink)" stroke-width="2"/><path d="M6 12l4 4 11-12" fill="none" stroke="var(--red)" stroke-width="3.5"/></svg>Floor strip and wax</li>
    <li><svg viewBox="0 0 24 24" aria-hidden="true"><rect x="2" y="4" width="17" height="17" fill="none" stroke="var(--ink)" stroke-width="2"/><path d="M6 12l4 4 11-12" fill="none" stroke="var(--red)" stroke-width="3.5"/></svg>Floor steaming</li>
  </ul>
  <ul class="services__list services__list--b">
    <li><svg viewBox="0 0 24 24" aria-hidden="true"><rect x="2" y="4" width="17" height="17" fill="none" stroke="var(--ink)" stroke-width="2"/><path d="M6 12l4 4 11-12" fill="none" stroke="var(--red)" stroke-width="3.5"/></svg>Janitorial services</li>
    <li><svg viewBox="0 0 24 24" aria-hidden="true"><rect x="2" y="4" width="17" height="17" fill="none" stroke="var(--ink)" stroke-width="2"/><path d="M6 12l4 4 11-12" fill="none" stroke="var(--red)" stroke-width="3.5"/></svg>Personal supervision</li>
    <li><svg viewBox="0 0 24 24" aria-hidden="true"><rect x="2" y="4" width="17" height="17" fill="none" stroke="var(--ink)" stroke-width="2"/><path d="M6 12l4 4 11-12" fill="none" stroke="var(--red)" stroke-width="3.5"/></svg>Quality control</li>
  </ul>
</div>
</body>
</html>
```